FLY/CRUISE PACAKGE TO THE ARCTIC TO SEE BIRD LIFE and POLAR BEARS

I am wanting to create a double sided A4 colour flyer (Finished size: 297 x 210mm) for a Fly/Cruise package from Australia to the Arctic.
The idea is that I would like the art work or design work done for the flyer that I can then send to a printer to do the printing of these flyers.

My business is a retail cruise travel agent that specializes in selling all-inclusive packages on luxury expedition ships and in this case I intend to promote this cruise to people that are interested in wildlife and also bird watching.

I will attach a copy of the full brochure from the cruise line Meridane Voyages that we will be using to give you more information on them and the cruise we are travelling on will be on page 38 and 39 of the brochure and I show you this because it gives you a map of the cruise.

I will also attach my logo so this can be included and a copy of the draft itinerary that I see as being the highlights however I am aware that we are limited on space and we need to get the key issues across and also as the trip is being marketed to bird watchers and wildlife enthusiasts then some good pictures of both a polar bear and let’s say a bird called a puffin and maybe a Reindeer.

We also need to show the costing's and what's included in the package.

And of course a call to action
All bookings and enquiries call Corbin

1-300-418-937
WavePath Pty Ltd

“I never forget you have a choice”

Target Market(s)

Travellers that are interested in Expedition cruising and are keen on seeing wildlife and birdlife

Industry/Entity Type

Travel Industry

Colors
0255a3
ec1f27
ffffff
0393ce

Requirements
Must have
• A picture od a Polar Bear / A Puffin
• It must look very professional as this trip is an expensive trip
Nice to have
• A picture of the ship "Tern Harbour"
• Bright and appealing appearance
• See the Polar Bears while officials still allow tourism to this area

```html
<!DOCTYPE html>
<html lang="en">
<head>
<meta charset="utf-8">
<title>West Spitsbergen and Polar Ice Edge Cruise – Flyer</title>
<link href="https://fonts.googleapis.com/css2?family=Source+Sans+3:wght@400;600;700&display=swap" rel="stylesheet">
<style>
:root{
  --navy:#0255a3;
  --deep:#0a3f86;
  --sky:#0393ce;
  --red:#ec1f27;
  --white:#ffffff;
  --ink:#3a3a3a;
  --stage:#e6e4e1;
  --rule:#b9c4d3;
}
*{box-sizing:border-box;margin:0;padding:0}
html,body{width:1200px;height:806px;overflow:hidden;background:var(--stage);font-family:"Source Sans 3",Arial,sans-serif;color:var(--ink)}
.sheet{position:absolute;top:35px;width:520px;height:736px;background:var(--white);overflow:hidden;box-shadow:0 2px 8px rgba(0,0,0,.18)}
.sheet--front{left:60px}
.sheet--back{left:620px}
.photo{position:absolute;background:linear-gradient(180deg,#6f8fb1 0%,#b9cde0 30%,#eef3f8 52%,#9fb6c9 70%,#3f6687 100%)}
.front-hero{left:0;top:0;width:520px;height:260px}
.swoosh{position:absolute;left:0;top:150px;width:520px;height:140px}
.circle{position:absolute;border-radius:50%;border:4px solid var(--white);box-shadow:0 1px 4px rgba(0,0,0,.35)}
.c-bear{background:radial-gradient(circle at 50% 45%,#f3efe4,#c7ccd4 65%,#8ea3b8)}
.c-group{background:radial-gradient(circle at 50% 55%,#d8262d,#e9eef3 60%,#aebfd0)}
.c-kayak{background:radial-gradient(circle at 50% 65%,#f2c21b,#2f6aa6 55%,#9db8d1)}
.c-walrus{background:radial-gradient(circle at 50% 60%,#8a6a4d,#d9252c 55%,#c5d3e0)}
.c-hikers{background:radial-gradient(circle at 50% 50%,#d8262d,#eef2f6 60%,#b7c7d6)}
.headline{position:absolute;text-align:center}
.headline h1{font-size:14.5px;font-weight:600;color:var(--deep);line-height:1.2}
.headline .dates{font-size:14px;font-weight:600;color:var(--red);line-height:1.3}
.col{position:absolute;width:222px;font-size:6.9px;line-height:1.25;text-align:justify}
.col p{margin-bottom:1px}
.day{display:block;height:22px;border-radius:11px;background:linear-gradient(90deg,var(--sky),var(--navy) 60%,var(--deep));color:var(--white);font-size:10px;font-weight:600;line-height:22px;padding-left:14px;margin:13px 0 16px;box-shadow:0 1px 2px rgba(0,0,0,.25)}
.footer{position:absolute;left:0;bottom:0;width:520px;height:60px}
.web{position:absolute;left:18px;bottom:9px;font-size:11.5px;font-weight:600;letter-spacing:.6px;color:var(--white)}
.brand{position:absolute;display:flex;align-items:center;gap:6px}
.brand-dot{width:20px;height:20px;border-radius:50%;background:var(--sky)}
.brand-name{font-size:22px;font-weight:700;color:var(--navy);letter-spacing:.5px;line-height:1}
.brand-tag{font-size:6.6px;font-weight:700;color:var(--navy);letter-spacing:.8px}
.back-hero{left:0;top:0;width:520px;height:270px}
.back-shape{position:absolute;left:0;top:0;width:520px;height:736px}
.badge{position:absolute;left:206px;top:214px;width:46px;height:34px;border-radius:6px;background:var(--navy)}
.details{position:absolute;left:17px;width:230px;font-size:6.8px;line-height:1.25;text-align:justify}
.details p{margin-bottom:5px}
.rule{position:absolute;left:17px;width:255px;height:1px;background:var(--rule)}
.panel{position:absolute;left:291px;width:212px;color:var(--white);font-size:7.2px;line-height:1.25;text-align:justify}
.panel h2{font-size:9px;font-weight:600;margin-bottom:10px}
.panel p{margin-bottom:8px}
.panel .panel-rule{height:1px;background:rgba(255,255,255,.6);margin:8px 0}
.signoff{position:absolute;right:16px;top:622px;text-align:right;color:var(--white);font-size:6.8px;line-height:1.6}
.signoff .gap{height:8px}
</style>
</head>
<body>

<section class="sheet sheet--front">
  <div class="photo front-hero" role="img" aria-label="Expedition ship Tern Harbour of Meridane Voyages cruising past arctic ice arches and snowy mountains"></div>
  <svg class="swoosh" viewBox="0 0 520 140" preserveAspectRatio="none" aria-hidden="true">
    <path d="M0 60 C140 40 320 30 520 20 L520 140 L0 140Z" fill="var(--sky)"/>
    <path d="M0 70 C150 52 320 44 520 36 L520 140 L0 140Z" fill="var(--navy)"/>
    <path d="M0 82 C150 66 320 62 520 58 L520 140 L0 140Z" fill="var(--white)"/>
  </svg>
  <div class="circle c-bear" style="left:173px;top:127px;width:96px;height:96px" role="img" aria-label="Polar bear on the ice"></div>
  <div class="circle c-group" style="left:290px;top:135px;width:92px;height:92px" role="img" aria-label="Travellers in red parkas relaxing on the snow"></div>
  <div class="circle c-kayak" style="left:399px;top:152px;width:92px;height:92px" role="img" aria-label="Guest paddling a yellow kayak among icebergs"></div>

  <div class="headline" style="left:95px;width:330px;top:244px">
    <h1>West Spitsbergen and Polar Ice Edge Cruise</h1>
    <div class="dates">Wednesday 27th June – 05 July Thursday 2018</div>
  </div>

  <div class="col" style="left:18px;top:304px">
    <span class="day">DAY 1:&nbsp; Longyearbyen, Svalbard</span>
    <p>Welcome to Longyearbyen, the administrative capital of the Norwegian territory of Svalbard and starting point of our expedition. After arriving via scheduled commercial flight service, you are free to explore this fascinating Arctic settlement. Be sure to see the excellent Svalbard Museum and take advantage of quality shopping and dining opportunities in the town center. Your hotel for the night has been arranged by us and is included in the price of the voyage.</p>
    <span class="day">DAY 2:&nbsp; Embarkation in Longyearbyen</span>
    <p>In the afternoon we welcome you aboard the luxury expedition ship M/V Tern Harbour. Explore the ship and get comfortable in your home away from home for the extraordinary adventure to come. Savour the anticipation of your Arctic dreams coming true as we slip our moorings and sail into a true wilderness where wildlife abounds. The scenery as we sail through Isfjorden on our first evening is spectacular and there is already the possibility of marine mammal encounters.</p>
    <span class="day">DAY 3-8:&nbsp; Exploration of West Spitsbergen</span>
    <p>This is a real expedition in a true High Arctic wilderness. As such, our route and exploration opportunities here are heavily dependent on the weather and sea ice conditions we encounter. Our experienced captain and expedition leader decide the itinerary and continually adjust plans as conditions and opportunities warrant. You can be sure that the best possible advantage will be taken of the circumstances presented to us by Nature in this wild and remote corner of the Arctic.</p>
    <p>Polar bears and other quintessential Arctic wildlife can be spotted anytime, anywhere in and around Svalbard. We exploit every opportunity to experience excellent wildlife viewing, to discover incredible scenery, and to walk in the footsteps of the historic polar expeditions that came before us.</p>
    <p>We anticipate exploring the spectacular fjords, coasts, and islands</p>
  </div>

  <div class="col" style="left:288px;top:320px">
    <p>in the northwestern part of Svalbard. This area contains the archipelago's most impressive scenery and some of the Arctic's best wildlife viewing opportunities. Deep fjords and narrow channels are flanked by jagged snowy mountain peaks. Immense tidewater glaciers calve icebergs into turquoise waters. On ice floes and on fast ice several species of seals watch vigilantly for polar bears. Fields of flowering tundra are home to grazing reindeer and playful Arctic fox. Bountiful inshore and offshore waters are home to walrus and a wide variety of whales. The whole area is alive with migratory birds, including numerous rare species, taking advantage of summer's fecundity in 24-hour daylight.</p>
    <p>And over it all presides the polar bear, monarch of the North. This wild corner of Svalbard is one of the best places in the world to observe polar bears hunting in their preferred habitat: the pack ice. We take the ship as close as safely possible to the jumbled and broken edge of the polar ice cap, where polar bears stalk the frozen sea in search of seals.</p>
    <p>To complete the Arctic experience we also explore places rich with history. Our area of exploration contains the historical remnants of whaling camps, coal mining operations, trappers' cabins, staging areas for historic attempts to discover the North Pole, and even an abandoned polar research station.</p>
    <p>Human habitation in this area can be found only at Ny Ålesund, a former mining town that is now home to an international community of Arctic researchers. This is one of the world's most northerly settlements, complete with museum, gift shop, and post office.</p>
    <p>The days are filled with memorable excursions, sumptuous meals, presentations by our experts, and enough stunning scenery and wildlife to fill your camera and overwhelm your emotions.</p>
    <span class="day">DAY 9:&nbsp; Disembarkation in Longyearbyen, Svalbard</span>
    <p>After breakfast we say farewell in the town of Longyearbyen, where we started. We provide a transfer to the airport or to the town center if you wish to spend more time here. As you look back on your wonderful experience in Svalbard, you may already be looking forward to your next incredible adventure to the ice!</p>
  </div>

  <svg class="footer" viewBox="0 0 520 60" preserveAspectRatio="none" aria-hidden="true">
    <path d="M0 26 L250 26 C285 26 300 46 340 60 L0 60Z" fill="var(--navy)"/>
    <path d="M0 26 L230 26 C260 26 270 40 300 60 L0 60Z" fill="var(--deep)"/>
    <path d="M470 60 C495 50 510 42 520 38 L520 60Z" fill="var(--navy)"/>
  </svg>
  <div class="web">WWW.WAVEPATH.COM.AU</div>
  <div class="brand" style="left:288px;top:668px">
    <span class="brand-dot"></span>
    <div><div class="brand-name">WAVEPATH</div><div class="brand-tag">Expedition Cruise Specialists Since 1998</div></div>
  </div>
</section>

<section class="sheet sheet--back">
  <div class="photo back-hero" role="img" aria-label="Expedition ship anchored in a calm bay beside icebergs and glaciated peaks, with a zodiac in the foreground"></div>
  <svg class="back-shape" viewBox="0 0 520 736" preserveAspectRatio="none" aria-hidden="true">
    <path d="M0 262 C100 250 200 232 278 222 L520 200 L520 736 L0 736Z" fill="var(--sky)"/>
    <path d="M0 268 C100 256 200 238 278 228 L520 214 L520 736 L0 736Z" fill="var(--white)"/>
    <path d="M278 228 C360 218 440 212 520 212 L520 736 L278 736Z" fill="var(--navy)"/>
    <path d="M278 400 C360 420 450 560 520 600 L520 736 L278 736Z" fill="var(--deep)" opacity=".55"/>
    <path d="M0 702 L240 702 C260 702 268 716 278 736 L0 736Z" fill="var(--deep)"/>
  </svg>
  <div class="circle c-walrus" style="left:305px;top:155px;width:96px;height:96px" role="img" aria-label="Guests in red parkas watching walrus on a beach"></div>
  <div class="circle c-hikers" style="left:413px;top:153px;width:96px;height:96px" role="img" aria-label="Hikers in red jackets exploring the snow"></div>
  <div class="badge" aria-hidden="true"></div>

  <div class="headline" style="left:17px;top:287px;text-align:left">
    <h1 style="font-size:12.5px">West Spitsbergen and Polar Ice Edge Cruise</h1>
    <div class="dates" style="font-size:12.5px">Wednesday 27th June - 05 July Thursday 2018</div>
  </div>

  <div class="rule" style="top:327px"></div>
  <div class="details" style="top:336px">
    <p>Sunday 24th June we fly from our Home Australian airport to Singapore.</p>
    <p>Singapore: The Harbourline Hotel or similar</p>
    <p>Check-in: 24 June out 26 June with late check out on the 26th. Return airport transfers. Full breakfast. City Tour. Dinner and nightlife tour at the Singapore Zoo.</p>
    <p>Tuesday 26th June we fly overnight from Singapore to Norway where we join are cruise package.</p>
  </div>
  <div class="rule" style="top:425px"></div>

  <div class="details" style="top:440px">
    <p>Thursday 5th July our cruise package finishes and we fly to our next destination:</p>
    <p>If you select to fly home to Australia we have included a 2 night stopover on the way home and you may select from Singapore or Hong Kong or Bangkok / transfers-breakfast and city tour included.</p>
    <p>Or ask for other options as the return is very flexible you may like to consider a Baltic cruise or a land based tour or a river cruise as an add on just ask us for options.</p>
    <p>Early Bird Fares available till end July 2017 or until sold out.</p>
    <p>Twin share<br>Outside cabin cost $11,999.00 per person.<br>Balcony cabin cost $13,999.00 per person.</p>
    <p>Single costings and costs to upgrade to a Suite on application.</p>
    <p>Deposit $4,000 per person due 14 days after confirmation and is non-refundable / Insurance quote will be given</p>
    <p>Final payment 01 March 2018</p>
  </div>

  <div class="brand" style="left:14px;top:648px">
    <span class="brand-dot"></span>
    <div><div class="brand-name">WAVEPATH</div><div class="brand-tag">Expedition Cruise Specialists Since 1998</div></div>
  </div>
  <div class="web">WWW.WAVEPATH.COM.AU</div>

  <div class="panel" style="top:262px">
    <h2>INCLUSIONS:</h2>
    <p>Return economy class airfare and taxes from your home Australian Airport</p>
    <p>All transfers<br>2.5 night Hotel package in Singapore<br>8 night cruise package that includes 1 nights pre-cruise hotel accommodation and the 7 night cruise<br>All meals and most expeditions whilst on board our ship The Tern Harbour<br>2.5 night stopover package on your return trip home to Australia</p>
    <div class="panel-rule"></div>
    <p>Wildlife that we may have the opportunity to see on our trip pending on weather conditions:<br>We will have daylight 24 hours each day during our cruise.<br>19 species of Mammal are known to be in the area that we are visiting &amp; some are:<br>Polar Bears / Walruses / Seals / Whales / Reindeer / Arctic Fox<br>30 Sea Bird species call Spitsbergen home during summer and some we are hoping to see are:<br>Atlantic Puffin / Snow Bunting / Pink-Footed Geese / Purple Sandpiper / Ptarmigan / Common Guillemot / Arctic Terns / Black Legged Kittiwake / Great Skua and if we are very lucky we may spot the Sabine Gull or a King Elder.<br>Whilst the above cannot be guaranteed it is know that most visitors do spot approximately 23 species during similar trips.</p>
  </div>

  <div class="signoff">
    Best Regards,<br>Corbin Hartley<br>Your Personal Travel Concierge
    <div class="gap"></div>
    1-300-418-937<br>WavePath Pty Ltd<br>PO Box 217, Glebe NSW 2037<br>(An Independent Travel Agency)<br>WWW.WAVEPATH.COM.AU
  </div>
</section>

</body>
</html>
```